Company Website for Vortel Insight, an open source data analytics company focused on relationship and li

I need a company/brand website for our new startup, Vortel Insight LLC. We are a company focused on using life pattern analysis techniques, looking at relationships and how relationships, attributes, and activity cluster to infer aggregate information about individuals and groups. Our focus is on improving the digital advertising market.

We have a company logo which I will upload shortly.

Target Market(s)

Digital Advertising

Number of Pages Required

3 page

Font styles to use
Sans Serif

Requirements
Must have
• An main page, about us, contact page.
Nice to have
• Vortel Insight relies on state of the art analytics applied to a the digital marketing space. While it is heavy in science, we also understand the art of influence. The website should have a scientific edge but also a flair that illustrates our focus on applying the hard science and analytics to influencing the behavior of people.

```html
<!DOCTYPE html>
<html lang="en">
<head>
<meta charset="utf-8">
<title>Vortel Insight</title>
<link href="https://fonts.googleapis.com/css2?family=Montserrat:wght@400;600;700;800&family=Lato:wght@400;700&display=swap" rel="stylesheet">
<style>
:root{
  --blue:#1e73be;
  --blue-dark:#0d3f82;
  --orange:#f7941d;
  --ink:#333;
  --muted:#666;
  --light:#f3f3f3;
  --footer:#0b0b0b;
  --footer-bar:#3a3a3a;
  --white:#fff;
}
*{box-sizing:border-box;margin:0;padding:0}
html,body{width:1200px;height:3922px;overflow:hidden}
body{font-family:"Lato",sans-serif;color:var(--ink);background:var(--white);position:relative}
.abs{position:absolute}

/* header */
.network-art{left:0;top:0;width:1200px;height:370px;background:linear-gradient(180deg,#eef3f9 0%,#ffffff 100%)}
.brand{left:300px;top:395px;display:flex;align-items:center;gap:12px}
.brand-mark{width:34px;height:34px;border-radius:50%;background:var(--orange)}
.brand-name{font-family:"Montserrat",sans-serif;font-weight:700;font-size:40px;color:var(--blue);letter-spacing:.5px}
.hero-title{left:175px;top:520px;font-family:"Montserrat",sans-serif;font-weight:700;font-size:47px;line-height:54px;color:var(--orange)}
.hero-sub{left:180px;top:635px;font-family:"Montserrat",sans-serif;font-weight:700;font-size:26px;color:var(--blue)}
.nav{left:178px;top:719px;display:flex;gap:42px;align-items:center;font-family:"Montserrat",sans-serif;font-size:17px;color:#444}
.nav .active{background:var(--blue);color:var(--white);padding:6px 18px;border-radius:16px}
.call{left:690px;top:698px;text-align:center;width:200px}
.call small{display:block;color:var(--blue);font-size:14px;font-weight:700}
.call strong{font-size:20px;color:var(--blue);font-weight:700;white-space:nowrap}
.follow{left:975px;top:698px;width:120px;text-align:center}
.follow small{display:block;color:var(--blue);font-size:14px;font-weight:700;margin-bottom:6px}
.dots{display:flex;gap:10px;justify-content:center}
.dots span{width:12px;height:12px;border-radius:50%;background:#888}

/* section label */
.section-title{display:flex;align-items:center;gap:8px;font-family:"Montserrat",sans-serif;font-weight:600;color:var(--blue)}
.section-title::before{content:"";width:14px;height:14px;background:var(--orange);flex:none}
.pill{display:inline-block;background:var(--orange);color:var(--white);font-size:11px;padding:4px 12px;border-radius:10px}

/* about */
.about{left:0;top:836px;width:1200px;height:486px;background:var(--light)}
.about-art{left:204px;top:80px;width:384px;height:312px;background:linear-gradient(135deg,#f7a54a,#4aa3df 55%,#7e56a6)}
.about-copy{left:627px;top:80px;width:380px}
.about-copy h2{font-size:28px;margin-bottom:12px}
.about-copy p{font-size:14px;line-height:22px;color:#444;margin-bottom:12px}
.about-copy .pill{margin-bottom:26px}

/* stats */
.stats{left:0;top:1328px;width:1200px;height:246px;background:linear-gradient(90deg,#0d3f82,#1e73be 50%,#0d3f82)}
.stat{top:78px;width:260px;text-align:center;color:var(--white)}
.stat b{display:block;font-family:"Montserrat",sans-serif;font-size:58px;font-weight:700;color:var(--orange);line-height:60px}
.stat span{font-size:18px}

/* services */
.services-title{left:0;top:1632px;width:1200px;justify-content:center;font-size:28px}
.arrow{width:32px;height:32px;background:var(--orange);display:flex;align-items:center;justify-content:center}
.card{top:1725px;width:230px;height:400px;background:var(--blue);border:4px solid var(--blue)}
.card-photo{height:222px;background:linear-gradient(135deg,#e8eef5,#b7c9dc)}
.card-label{margin:6px 0;background:var(--orange);color:var(--white);text-align:center;font-family:"Montserrat",sans-serif;font-weight:700;font-size:17px;padding:9px 0}
.card p{color:var(--white);font-size:13px;line-height:17px;padding:6px 12px}
.card .pill{position:absolute;left:50%;bottom:-14px;transform:translateX(-50%)}

/* testimonials */
.clients{left:0;top:2253px;width:1200px;height:322px;background:var(--light)}
.clients-intro{left:178px;top:92px;width:280px}
.clients-intro h2{font-size:25px;line-height:30px;margin-bottom:14px}
.clients-intro p{font-size:13px;line-height:18px;color:#555;padding-left:22px}
.quote{top:94px;width:242px;height:150px;padding:14px 16px;color:var(--white);border-radius:3px}
.quote .who{display:flex;gap:12px;align-items:center;margin-bottom:8px}
.avatar{width:44px;height:44px;border-radius:50%;background:#d9c3a8;border:3px solid var(--white);flex:none}
.who b{display:block;font-size:14px}
.who small{font-size:10px}
.quote p{font-size:12px;line-height:16px}

/* newsletter */
.newsletter{left:0;top:2601px;width:1200px;height:65px;background:var(--blue)}
.nl-icon{left:200px;top:11px;width:44px;height:44px;border-radius:50%;background:var(--orange)}
.nl-label{left:260px;top:17px;font-family:"Montserrat",sans-serif;font-weight:600;font-size:24px;color:var(--orange)}
.nl-input{left:549px;top:18px;width:308px;height:30px;background:var(--white);font-size:12px;color:#999;padding:8px 12px}
.nl-button{left:865px;top:18px;width:136px;height:30px;background:var(--orange);color:var(--white);font-family:"Montserrat",sans-serif;font-weight:700;font-size:13px;text-align:center;line-height:30px}

/* team */
.team-title{left:0;top:2728px;width:1200px;justify-content:center;font-size:28px}
.member{top:2815px;width:184px;text-align:center}
.member-photo{height:160px;background:linear-gradient(180deg,#9dc1e6,#3f7fc1)}
.member h3{font-family:"Montserrat",sans-serif;font-size:20px;color:var(--blue);margin-top:12px;font-weight:600}
.member small{font-size:13px;color:#777}
.member .dots{margin-top:8px;gap:6px}
.member .dots span{width:14px;height:14px;background:none;border:1px solid #aaa}

/* banner */
.banner{left:0;top:3124px;width:1200px;height:235px;background:linear-gradient(90deg,#e98a14,#f7a43a 60%,#e4891a)}
.banner-art{left:810px;top:20px;width:340px;height:200px;background:radial-gradient(circle at 50% 50%,rgba(255,255,255,.25),rgba(0,0,0,.06) 70%);border-radius:8px}
.banner-copy{left:199px;top:40px;width:590px;color:var(--white)}
.banner-copy h2{font-family:"Montserrat",sans-serif;font-size:22px;line-height:28px;font-weight:700;margin-bottom:8px}
.banner-copy p{font-size:12px;line-height:16px}

/* partners */
.partners{left:0;top:3372px;width:1200px;height:170px}
.partner{top:58px;width:200px;text-align:center;font-family:"Montserrat",sans-serif;font-weight:800;font-size:40px;color:#a9a9a9}

/* footer */
.footer{left:0;top:3555px;width:1200px;height:314px;background:var(--footer);color:#ccc}
.footer-brand{left:100px;top:70px;display:flex;align-items:center;gap:8px}
.footer-brand .brand-mark{width:20px;height:20px}
.footer-brand .brand-name{font-size:24px}
.footer-about{left:100px;top:148px;width:240px;font-size:12px;line-height:17px;color:#ddd}
.fcol{top:70px;padding-left:22px;border-left:1px solid #444;height:200px}
.fcol h4{font-family:"Montserrat",sans-serif;font-size:18px;letter-spacing:1px;color:var(--blue);padding-bottom:10px;border-bottom:1px solid #444;margin-bottom:14px;width:190px}
.fcol li{list-style:none;font-size:14px;line-height:27px;color:#ddd}
.fcol li::before{content:"›";color:var(--orange);margin-right:8px}
.contact-list li{font-size:12px;line-height:18px;margin-bottom:6px}
.contact-list li::before{content:"●";font-size:8px;color:var(--blue)}
.fcol .dots{justify-content:flex-start;gap:14px}
.fcol .dots span{background:var(--white)}
.fcol .call-title{margin-top:34px;color:var(--orange);font-family:"Montserrat",sans-serif;font-weight:700;font-size:19px}
.fcol .call-number{color:var(--white);font-family:"Montserrat",sans-serif;font-weight:700;font-size:22px}
.footer-bar{left:0;top:3869px;width:1200px;height:53px;background:var(--footer-bar);color:#ccc;text-align:center;font-size:14px;line-height:53px}
</style>
</head>
<body>

<div class="abs network-art" role="img" aria-label="Network of connected nodes with social media icons"></div>
<div class="abs brand"><span class="brand-mark"></span><span class="brand-name">Vortel Insight</span></div>
<h1 class="abs hero-title">WE UNDERSTAND<br>THE ART OF INFLUENCE.</h1>
<p class="abs hero-sub">SOLUTION FOR EVERY BUSINESS</p>
<nav class="abs nav">
  <span class="active">Home</span><span>About Us</span><span>Our Services</span><span>Contact Us</span>
</nav>
<div class="abs call"><small>Call us</small><strong>+256 400 118820</strong></div>
<div class="abs follow"><small>Follow us</small><div class="dots"><span></span><span></span><span></span><span></span></div></div>

<section class="abs about">
  <div class="abs about-art" role="img" aria-label="Illustration of a laptop and a head with colourful data icons"></div>
  <div class="abs about-copy">
    <h2 class="section-title">About Us</h2>
    <p>We are a company focused on using life pattern analysis techniques, looking at relationships and how relationships, attributes, and activity cluster to infer aggregate information about individuals and groups. Our focus is on improving the digital advertising market.</p>
    <span class="pill">Read More</span>
    <h2 class="section-title">Vision</h2>
    <p>We focus on applying the hard science and analytics to influencing the behavior of people.</p>
    <span class="pill">Read More</span>
  </div>
</section>

<section class="abs stats" role="img" aria-label="Blue background of binary digits">
  <div class="abs stat" style="left:131px"><b>50%</b><span>growth in sales</span></div>
  <div class="abs stat" style="left:466px"><b>250</b><span>plus succesful<br>campaigns</span></div>
  <div class="abs stat" style="left:808px"><b>80%</b><span>Repeat clients</span></div>
</section>

<h2 class="abs section-title services-title">Our Services</h2>
<div class="abs arrow" style="left:0;top:1895px"><svg width="12" height="16"><path d="M10 2 3 8l7 6" stroke="#fff" stroke-width="3" fill="none"/></svg></div>
<div class="abs arrow" style="left:1168px;top:1895px"><svg width="12" height="16"><path d="M2 2l7 6-7 6" stroke="#fff" stroke-width="3" fill="none"/></svg></div>
<article class="abs card" style="left:204px">
  <div class="card-photo" role="img" aria-label="Team working over printed charts"></div>
  <div class="card-label">VARIETATES AUTEM</div>
  <p>Lorem ipsum dolor sit amet, consectetur adipiscing elit. Quid autem habent admirationis, cum prope accesseris? An hoc usque quaque, aliter in vita? Non igitur</p>
  <span class="pill">Read More</span>
</article>
<article class="abs card" style="left:489px">
  <div class="card-photo" role="img" aria-label="Colleagues discussing at a laptop"></div>
  <div class="card-label">FORTUNAE FACILE</div>
  <p>Lorem ipsum dolor sit amet, consectetur adipiscing elit. Quid autem habent admirationis, cum prope accesseris? An hoc usque quaque, aliter in vita? Non igitur</p>
  <span class="pill">Read More</span>
</article>
<article class="abs card" style="left:774px">
  <div class="card-photo" role="img" aria-label="Analytics dashboard on a screen"></div>
  <div class="card-label">EODEM FLUMINE</div>
  <p>Lorem ipsum dolor sit amet, consectetur adipiscing elit. Quid autem habent admirationis, cum prope accesseris? An hoc usque quaque, aliter in vita? Non igitur</p>
  <span class="pill">Read More</span>
</article>

<section class="abs clients">
  <div class="abs clients-intro">
    <h2 class="section-title">What our Client's<br>Say about us</h2>
    <p>Lorem ipsum dolor sit amet, consectetur adipiscing elit. Quid autem habent admirationis, cum prope accesseris? An hoc usque quaque, aliter in vita? Non igitur de improbo, sed de callido</p>
  </div>
  <div class="abs quote" style="left:497px;background:var(--blue)">
    <div class="who"><span class="avatar" role="img" aria-label="Client portrait"></span><div><b>Owen Caldwell</b><small>Marketing, Brightpath Inc</small></div></div>
    <p>“ Lorem ipsum dolor sit amet, consectetur adipiscing elit. Quid autem habent admirationis, cum prope accesseris? ”</p>
  </div>
  <div class="abs quote" style="left:758px;background:var(--orange)">
    <div class="who"><span class="avatar" role="img" aria-label="Client portrait"></span><div><b>Rhys Partridge</b><small>Production, Corvel Co</small></div></div>
    <p>“ Lorem ipsum dolor sit amet, consectetur adipiscing elit. Quid autem habent admirationis, cum prope accesseris? ”</p>
  </div>
</section>

<section class="abs newsletter">
  <div class="abs nl-icon"><svg width="44" height="44"><rect x="13" y="15" width="18" height="13" fill="none" stroke="#fff" stroke-width="2"/><path d="M13 15l9 7 9-7" fill="none" stroke="#fff" stroke-width="2"/></svg></div>
  <div class="abs nl-label">News letter Signup</div>
  <svg class="abs" style="left:505px;top:14px" width="24" height="38"><path d="M4 3l14 16L4 35" stroke="#fff" stroke-width="4" fill="none"/></svg>
  <div class="abs nl-input">Enter Your Email</div>
  <div class="abs nl-button">SUBSCRIBE</div>
</section>

<h2 class="abs section-title team-title">Meet Our Expert</h2>
<div class="abs arrow" style="left:0;top:2880px"><svg width="12" height="16"><path d="M10 2 3 8l7 6" stroke="#fff" stroke-width="3" fill="none"/></svg></div>
<div class="abs arrow" style="left:1168px;top:2880px"><svg width="12" height="16"><path d="M2 2l7 6-7 6" stroke="#fff" stroke-width="3" fill="none"/></svg></div>
<div class="abs member" style="left:204px"><div class="member-photo" role="img" aria-label="Portrait of team member"></div><h3>Lena Marwick</h3><small>Founder</small><div class="dots"><span></span><span></span><span></span><span></span></div></div>
<div class="abs member" style="left:408px"><div class="member-photo" role="img" aria-label="Portrait of team member"></div><h3>Dara Quill</h3><small>Partner</small><div class="dots"><span></span><span></span><span></span><span></span></div></div>
<div class="abs member" style="left:614px"><div class="member-photo" role="img" aria-label="Portrait of team member"></div><h3>Tomas Healy</h3><small>CEO</small><div class="dots"><span></span><span></span><span></span><span></span></div></div>
<div class="abs member" style="left:818px"><div class="member-photo" role="img" aria-label="Portrait of team member"></div><h3>Nora Vance</h3><small>Consultant</small><div class="dots"><span></span><span></span><span></span><span></span></div></div>

<section class="abs banner">
  <div class="abs banner-art" role="img" aria-label="Hand selecting one person from a network of people"></div>
  <div class="abs banner-copy">
    <h2>Vortel Insight relies on state of the art analytics applied to a the digital marketing space.</h2>
    <p>Lorem ipsum dolor sit amet, consectetur adipiscing elit. Quid autem habent admirationis, cum prope accesseris? An hoc usque quaque, aliter in vita? Non igitur de improbo, sed de callido improbo quaerimus, qualis Q. Nam quibus rebus efficiuntur voluptates, eae non sunt in potestate sapientis. Negare non possum. Huic mori optimum esse propter desperationem sapientiae, illi propter spem vivere. Quid enim me prohiberet Epicureum esse, si probarem, quae ille</p>
  </div>
</section>

<section class="abs partners">
  <div class="abs arrow" style="left:0;top:70px"><svg width="12" height="16"><path d="M10 2 3 8l7 6" stroke="#fff" stroke-width="3" fill="none"/></svg></div>
  <div class="abs arrow" style="left:1168px;top:70px"><svg width="12" height="16"><path d="M2 2l7 6-7 6" stroke="#fff" stroke-width="3" fill="none"/></svg></div>
  <div class="abs partner" style="left:161px">Halvern</div>
  <div class="abs partner" style="left:384px">Mardale</div>
  <div class="abs partner" style="left:606px">Quenta</div>
  <div class="abs partner" style="left:828px">Solvik</div>
</section>

<footer class="abs footer">
  <div class="abs footer-brand"><span class="brand-mark"></span><span class="brand-name">Vortel Insight</span></div>
  <p class="abs footer-about">Lorem ipsum dolor sit amet, consectetur adipiscing elit. Quid autem habent admirationis, cum prope accesseris? An hoc usque quaque, aliter in vita? Non igitur de improbo, sed de callido improbo quaerimus.</p>
  <div class="abs fcol" style="left:400px">
    <h4>QUICK LINKS</h4>
    <ul><li>Home</li><li>About Us</li><li>Our people</li><li>Services</li><li>Contact Us</li></ul>
  </div>
  <div class="abs fcol contact-list" style="left:622px">
    <h4>CONTACT</h4>
    <ul><li>2240 Linden Ave<br>Brookfield, IL 60513</li><li>+256 400 118820</li><li>+256 400 118821</li><li>hello@vortelinsight.com</li><li>www.vortelinsight.com</li></ul>
  </div>
  <div class="abs fcol" style="left:894px">
    <h4>FOLLOW US ON</h4>
    <div class="dots"><span></span><span></span><span></span><span></span></div>
    <div class="call-title">CALL US ON</div>
    <div class="call-number">+256 400 118820</div>
  </div>
</footer>
<div class="abs footer-bar">© 2017 Vortel Insight &nbsp;|&nbsp; Privacy Policy &nbsp;|&nbsp; User Agreement</div>

</body>
</html>
```